Non fiction book cover. The book advises how to get a new job.

The book size will be 20cm high by 13cm wide and I need a front cover which can wrap around to the back. This book has a serious message, but I've tried to make it quite light to read and accessible. So I don't want a cover that is too dour or serious and not frivolous either. At the end of the project, I will need a high resolution 3D image of the book, included as part of the package.<br/>The Title of the book is:- "Past Your Prime? Hunting for the Next Role?<br/>by Gerald Whitcombe-Prynne".<br/>I am thinking of a light yellow background, with a striking image to attract attention. The image and words should be clear and sharp.<br/>Here is the, BACK COVER wording.<br/>"This book tells you clearly and simply the steps that you need to take, to get a job, once you’re over 50.<br/>It advises you on the techniques to use to write a killer CV.<br/>It explains how to ensure that your CV attention.<br/>It shows the best way to approach your local job agency.<br/>It demonstrates the best way to use your network.<br/><br/>This book, written by someone with 30 years’ experience in the recruitment industry, gives you ALL the answers.<br/>Whether you are a top executive or someone after some local part time work, then this book is for you. <br/>With the help of this book you will secure your next position.<br/>

Target Market(s)

UK, over 50s, male and female.

Font styles to use
Serif

Colors
fbee3e

Requirements
Must have
• A clear uncluttered cover.
Should not have
• Fussy and over complicated

```html
<!DOCTYPE html>
<html lang="en">
<head>
<meta charset="utf-8">
<title>Past Your Prime? — Gerald Whitcombe-Prynne</title>
<link rel="stylesheet" href="https://fonts.googleapis.com/css2?family=Playfair+Display:wght@600&family=Tinos&family=Shadows+Into+Light&display=swap">
<style>
  :root {
    --page-bg: #ffffff;
    --cover-yellow: #f9ec45;
    --ink: #3b3b3b;
    --script-ink: #2e2e2e;
    --art-top: #dcdade;
    --art-mid: #c9e2ec;
    --art-bottom: #bfe0ec;
  }
  * { margin: 0; padding: 0; box-sizing: border-box; }
  html, body {
    width: 1200px;
    height: 1106px;
    overflow: hidden;
    background: var(--page-bg);
  }
  .canvas {
    position: relative;
    width: 1200px;
    height: 1106px;
  }
  .cover {
    position: absolute;
    left: 275px;
    top: 53px;
    width: 650px;
    height: 1000px;
    background: var(--cover-yellow);
    overflow: hidden;
  }
  .author {
    position: absolute;
    top: 34px;
    left: 0;
    width: 100%;
    text-align: center;
    font-family: "Tinos", serif;
    font-size: 35px;
    letter-spacing: -0.6px;
    color: var(--ink);
  }
  .title {
    position: absolute;
    top: 100px;
    left: 16px;
    right: 16px;
    font-family: "Playfair Display", serif;
    font-weight: 600;
    color: var(--ink);
    line-height: 0.92;
  }
  .title-line-one {
    display: block;
    font-size: 104px;
    letter-spacing: -1px;
    white-space: nowrap;
    text-align: center;
  }
  .title-line-two {
    display: block;
    text-align: right;
    font-size: 150px;
    letter-spacing: -2px;
    white-space: nowrap;
  }
  .subtitle {
    position: absolute;
    top: 540px;
    left: 400px;
    width: 230px;
    text-align: center;
    font-family: "Shadows Into Light", cursive;
    font-size: 62px;
    line-height: 1.08;
    color: var(--script-ink);
  }
  .subtitle span { display: block; white-space: nowrap; }
  .cover-illustration {
    position: absolute;
    left: 0;
    bottom: 0;
    width: 380px;
    height: 510px;
  }
</style>
</head>
<body>
<div class="canvas">
  <div class="cover">
    <p class="author">Gerald Whitcombe-Prynne</p>
    <h1 class="title">
      <span class="title-line-one">PAST YOUR</span>
      <span class="title-line-two">PRIME?</span>
    </h1>
    <p class="subtitle"><span>Hunting</span><span>for the</span><span>Next Role?</span></p>
    <svg class="cover-illustration" viewBox="0 0 380 510" role="img" aria-label="Illustration of a grey-haired older woman in glasses, a light blue shirt with yellow braces and neck scarf, shrugging with one hand raised">
      <defs>
        <linearGradient id="artTone" x1="0" y1="0" x2="0" y2="1">
          <stop offset="0" stop-color="var(--art-top)"/>
          <stop offset="0.45" stop-color="var(--art-mid)"/>
          <stop offset="1" stop-color="var(--art-bottom)"/>
        </linearGradient>
      </defs>
      <path d="M0 40 Q0 0 40 0 L340 0 Q380 0 380 40 L380 510 L0 510 Z" fill="url(#artTone)"/>
    </svg>
  </div>
</div>
</body>
</html>
```